Wellness Company needs 2 updated pages for our powerpoint

1 page of our powerpoint needs to be split into 2 pages. I have uploaded an image of it all on 1 page, the left side needs to be on 1 page and the right side needs to be on a separate page. I also uploaded images of the top & bottom since it is so blurry. Landscape view, please. Don't worry about the bottom of the page design since that is our template.

Target Market(s)

Wellness and Business

Industry/Entity Type

Health And Wellness

Requirements
Must have
• Clear wording and bold font.
Nice to have
• Clear circles and images

```html
<!DOCTYPE html>
<html lang="en">
<head>
<meta charset="utf-8">
<title>Compensation Plan at a Glance</title>
<link rel="stylesheet" href="https://fonts.googleapis.com/css2?family=Montserrat:wght@400;500;600;700;800&display=swap">
<style>
:root{
  --green:#7dc21e;
  --green-dark:#4e9a12;
  --green-light:#e9f6d4;
  --orange:#f7941d;
  --orange-dark:#d86a0c;
  --brown:#7a4a12;
  --grey:#777;
  --grey-light:#bbb;
  --line:#e3e3e3;
  --white:#fff;
  --bg:#f2f2f2;
}
*{margin:0;padding:0;box-sizing:border-box}
html,body{width:1000px;height:1200px;overflow:hidden;background:var(--bg);font-family:'Montserrat',sans-serif}
.slide{position:absolute;left:0;width:1000px;background:var(--white);box-shadow:0 1px 4px rgba(0,0,0,.15)}
.slide--one{top:22px;height:563px}
.slide--two{top:602px;height:563px}
.header-band{position:absolute;left:0;height:50px;width:452px;background:linear-gradient(90deg,var(--green),var(--green-dark));clip-path:polygon(0 0,100% 0,93% 100%,0 100%);color:var(--white);font-weight:700;font-size:19px;display:flex;align-items:center;padding-left:30px;letter-spacing:.2px}
.brand{position:absolute;left:462px;display:flex;align-items:center;gap:6px;color:var(--green-dark);font-weight:700;font-size:20px}
.brand-dot{width:14px;height:14px;border-radius:50%;background:var(--green)}
.card{position:absolute;background:var(--white);box-shadow:0 2px 10px rgba(0,0,0,.12)}
.card-tab{position:absolute;left:0;top:0;width:48px;height:48px;background:linear-gradient(135deg,var(--green-dark),var(--green));clip-path:polygon(0 0,100% 0,0 100%)}
.card-tab span{position:absolute;left:10px;top:5px;color:var(--white);font-weight:700;font-size:14px}
.card-title{position:absolute;color:var(--green);font-weight:700;font-size:19px}
.subtitle{color:var(--orange);font-size:13px;font-weight:400;margin-top:2px}
.price-row{position:absolute;left:45px;width:272px;display:flex;justify-content:space-between;font-size:12px;color:var(--grey)}
.price-row--keep{left:38px;width:332px;background:var(--green-light);border-top:2px solid var(--green);height:30px;align-items:center;padding:0 8px 0 7px;color:var(--green-dark);font-weight:700}
.price-row--keep span:last-child{margin-right:45px}
.tree-lines{position:absolute;stroke:var(--grey-light);stroke-width:1;fill:none}
.node{position:absolute;width:40px;height:40px;border-radius:50%;border:2.5px solid var(--green);background:var(--white);display:flex;align-items:center;justify-content:center;font-weight:700;font-size:12px;color:var(--grey)}
.node--mid{color:var(--brown)}
.node--top{color:var(--grey-light)}
.node--head{width:38px;height:38px;border:none;background:var(--green);color:var(--white)}
.note{position:absolute;color:var(--orange);font-size:13px;line-height:1.25}
.callout{position:absolute;background:var(--orange);color:var(--white);font-size:10px;line-height:1.05;padding:8px;width:117px;box-shadow:2px 2px 6px rgba(0,0,0,.2)}
.callout::before{content:"";position:absolute;left:-8px;top:14px;border:6px solid transparent;border-right:8px solid var(--orange);border-left:none}
.divider{position:absolute;width:1px;background:var(--line)}
.table-head{position:absolute;top:64px;color:var(--orange);font-weight:700;font-size:12px;width:98px;text-align:center}
.row-num{position:absolute;left:33px;color:var(--orange);font-weight:700;font-size:12px}
.row-line{position:absolute;left:25px;height:1px;background:var(--line)}
.bar{position:absolute;background:linear-gradient(90deg,var(--green),var(--green-dark));color:var(--white);font-weight:700;font-size:16px;display:flex;align-items:center;justify-content:center}
.bar--orange{background:linear-gradient(90deg,var(--orange-dark),var(--orange))}
.footnotes{position:absolute;left:33px;top:342px;color:var(--orange);font-size:11px;line-height:1.2}
.qual-band{position:absolute;left:500px;top:116px;width:292px;height:32px;background:linear-gradient(90deg,var(--green),var(--green-dark));clip-path:polygon(0 0,100% 0,96% 100%,0 100%);color:var(--white);font-weight:700;font-size:17px;letter-spacing:4px;padding-left:36px;display:flex;align-items:center}
.qual{position:absolute;left:545px;height:60px;width:420px}
.qual-num{position:absolute;left:2px;top:10px;color:var(--green);font-weight:700;font-size:27px}
.qual-rule{position:absolute;left:55px;top:-6px;width:2px;height:58px;background:var(--line)}
.qual-title{position:absolute;left:80px;top:0;color:var(--green-dark);font-weight:700;font-size:11px}
.qual-list{position:absolute;left:80px;top:16px;list-style:none;font-size:9.5px;color:var(--grey);line-height:1.15}
.qual-list li::before{content:"• "}
.disclaimer{position:absolute;left:508px;top:505px;color:var(--green-dark);font-size:9.5px;line-height:1.25}
</style>
</head>
<body>

<section class="slide slide--one">
  <div class="header-band" style="top:23px">COMPENSATION PLAN AT A GLANCE</div>
  <div class="brand" style="top:38px"><span class="brand-dot"></span>Tevrolin</div>

  <div class="card" style="left:55px;top:118px;width:420px;height:182px">
    <div class="card-tab"><span>1</span></div>
    <div class="card-title" style="left:45px;top:18px">DIRECT SELLING<div class="subtitle">Sell the product. Keep the profit</div></div>
    <div class="price-row" style="top:82px"><span>Suggested retail :</span><span>$34.95</span></div>
    <div class="price-row" style="top:113px"><span>Wholesale:</span><span>$24.95</span></div>
    <div class="price-row price-row--keep" style="top:135px"><span>You keep</span><span>$10.00</span></div>
  </div>

  <div class="card" style="left:540px;top:118px;width:422px;height:182px">
    <div class="card-tab"><span>2</span></div>
    <div class="card-title" style="left:47px;top:18px">FAST START BONUS</div>
    <svg class="tree-lines" style="left:0;top:0" width="422" height="182"><path d="M133 86V101M72 101H193M72 101V112M133 101V112M193 101V112"/></svg>
    <div class="node node--head" style="left:114px;top:50px">You</div>
    <div class="node" style="left:52px;top:114px">$10</div>
    <div class="node node--mid" style="left:113px;top:114px">$20</div>
    <div class="node node--top" style="left:173px;top:114px">$40</div>
    <div class="note" style="left:243px;top:102px;width:150px">Earn up to <b>$40</b> for each silver, gold or platinum package</div>
  </div>

  <div class="card" style="left:63px;top:325px;width:899px;height:210px">
    <div class="card-tab"><span>3</span></div>
    <div class="card-title" style="left:47px;top:20px">LEADERSHIP BONUS</div>
    <div class="divider" style="left:290px;top:50px;height:120px"></div>
    <div class="divider" style="left:590px;top:50px;height:120px"></div>
    <svg class="tree-lines" style="left:0;top:0" width="899" height="210"><path d="M87 94V112M37 112H137M37 112V124M87 112V124M137 112V124M379 94V112M328 112H428M328 112V124M379 112V124M428 112V124M678 94V112M627 112H729M627 112V124M678 112V124M729 112V124"/></svg>
    <div class="node node--head" style="left:68px;top:57px">MBO</div>
    <div class="node" style="left:17px;top:124px">$10</div>
    <div class="node node--mid" style="left:67px;top:124px">$20</div>
    <div class="node node--top" style="left:117px;top:124px">$40</div>
    <div class="callout" style="left:155px;top:55px">MBOs earn up to $10,$20 or $40 per enrollment package sold</div>
    <div class="node node--head" style="left:360px;top:57px">SBO</div>
    <div class="node" style="left:308px;top:124px">$20</div>
    <div class="node node--mid" style="left:359px;top:124px">$40</div>
    <div class="node node--top" style="left:408px;top:124px">$80</div>
    <div class="callout" style="left:454px;top:55px">SBOs earn up to $20,$40 or $80 per enrollment package sold. SBO leadership bonus may be split between different leaders. MBOs and SBOs will split the difference between bonuses</div>
    <div class="node node--head" style="left:659px;top:57px">EBO</div>
    <div class="node" style="left:607px;top:124px">$40</div>
    <div class="node node--mid" style="left:658px;top:124px">$80</div>
    <div class="node node--top" style="left:709px;top:124px">$160</div>
    <div class="callout" style="left:760px;top:55px">EBOs earn up to $40,$80 or $160 per enrollment package sold.EBO leadership bonus may be split between different leaders. MBOs, SBOs and EBOs will split the difference between bonuses</div>
  </div>
</section>

<section class="slide slide--two">
  <div class="header-band" style="top:23px">COMPENSATION PLAN AT A GLANCE</div>
  <div class="brand" style="top:38px"><span class="brand-dot"></span>Tevrolin</div>

  <div class="card" style="left:22px;top:116px;width:468px;height:422px">
    <div class="card-tab"><span>3</span></div>
    <div class="card-title" style="left:46px;top:20px">UNILEVEL COMMISSION</div>
    <div class="table-head" style="left:55px">IBO</div>
    <div class="table-head" style="left:153px">MBO</div>
    <div class="table-head" style="left:251px">SBO</div>
    <div class="table-head" style="left:349px">EBO/REBO</div>
    <div class="row-line" style="top:112px;width:30px"></div>
    <div class="row-line" style="top:142px;width:30px"></div>
    <div class="row-line" style="top:172px;width:130px"></div>
    <div class="row-line" style="top:202px;width:130px"></div>
    <div class="row-line" style="top:232px;width:228px"></div>
    <div class="row-line" style="top:262px;width:228px"></div>
    <div class="row-line" style="top:292px;width:326px"></div>
    <div class="row-line" style="top:322px;width:424px"></div>
    <div class="row-num" style="top:90px">1</div>
    <div class="row-num" style="top:120px">2</div>
    <div class="row-num" style="top:150px">3</div>
    <div class="row-num" style="top:180px">4</div>
    <div class="row-num" style="top:210px">5</div>
    <div class="row-num" style="top:240px">6</div>
    <div class="row-num" style="top:270px">7</div>
    <div class="row-num" style="top:300px">8</div>
    <div class="bar" style="left:55px;top:87px;width:98px;height:55px">5%</div>
    <div class="bar" style="left:153px;top:87px;width:98px;height:115px">5%</div>
    <div class="bar" style="left:251px;top:87px;width:98px;height:175px">5%</div>
    <div class="bar" style="left:349px;top:87px;width:98px;height:205px">5%</div>
    <div class="bar bar--orange" style="left:349px;top:293px;width:98px;height:29px">10%</div>
    <div class="footnotes">IBOs earn 5% commission on all sales 2 levels deep<br>MBOs earn 5% commission on all sales 4 levels deep<br>SBOs earn 5% commission on all sales 6 levels deep<br>EBOs earn 5% commission on all sales 7 levels deep</div>
  </div>

  <div class="qual-band">QUALIFICATIONS</div>

  <div class="qual" style="top:170px">
    <div class="qual-num">01</div><div class="qual-rule"></div>
    <div class="qual-title">Independent Business Owner (IBO)</div>
    <ul class="qual-list"><li>Enroll as an Active Independent Business Owner</li><li>After your first month to remain active you must personally<br>&nbsp;&nbsp;maintain a minimum of25 business volume &amp; subscribe to autoship.</li></ul>
  </div>
  <div class="qual" style="top:247px">
    <div class="qual-num">02</div><div class="qual-rule"></div>
    <div class="qual-title">Managing Business Owner (MBO1</div>
    <ul class="qual-list"><li>Be an active IBO and personally maintain 50 business volume</li><li>Personally Sponsor 8 IBO's. Each of them must be active.</li></ul>
  </div>
  <div class="qual" style="top:309px">
    <div class="qual-num">03</div><div class="qual-rule"></div>
    <div class="qual-title">Senior Business Owner (SBO)</div>
    <ul class="qual-list"><li>Be an Active IBO and personally acquire 100 business volume</li><li>Promote 3 MBO's in 3 Separate Legs</li><li>Maintain '1500 combined business volume for entire downline</li></ul>
  </div>
  <div class="qual" style="top:376px">
    <div class="qual-num">04</div><div class="qual-rule"></div>
    <div class="qual-title">Executive Business Owner (EBO)</div>
    <ul class="qual-list"><li>Be an Active IBO and personally maintain 200 business volume</li><li>Promote 3 SBO's in 3 Separate Legs</li><li>Maintain 5000 combined business volume for entire downline</li></ul>
  </div>
  <div class="qual" style="top:443px">
    <div class="qual-num">05</div><div class="qual-rule"></div>
    <div class="qual-title">Regional Executive Business Owner (REBO)</div>
    <ul class="qual-list"><li>Be an Active IBO and personally maintain 400 business volume</li><li>Promote 3 EBO's in 3 Separate Legs</li><li>Maintain 15000 combined business volume for entire downline</li></ul>
  </div>

  <div class="disclaimer">All requirements must be met lo stay commissionable within that rank<br>This is an example only, see full comp plan for details.</div>
</section>

</body>
</html>
```